Flooring & Interior Design showroom

Just bought this business- Kestrel Lane Flooring & Interiors. Love our logo (we are on Kestrel Lane )and colors
Forest green, gold and black
Love that the back lists everything we do. We no longer have plenotilex but need to add in LVP/ SPC and need to take out vantor shadehub logo at the bottom and use the quib logo instead (maybe? open to suggestions)

Not in love with our cards- I want a higher end look
I hate the gradient poop color we have now.
Would love if they were all black - maybe or ??
or had a foil or embossing?

```html
<!DOCTYPE html>
<html lang="en">
<head>
<meta charset="utf-8">
<title>Kestrel Lane Flooring &amp; Interiors — Stationery</title>
<link rel="stylesheet" href="https://fonts.googleapis.com/css2?family=Lato:wght@400;700&family=Pinyon+Script&display=swap">
<style>
  :root{
    --backdrop:#2b2e36;
    --paper:#dcdde4;
    --forest:#1f5030;
    --forest-deep:#143a22;
    --forest-light:#3f7a4f;
    --gold:#c9a24a;
    --gold-light:#e3c577;
    --card-black:#242427;
    --ink:#1d1d1f;
    --muted:#666a70;
    --rule:#8a8d93;
    --window:#c4c5cb;
  }
  *{box-sizing:border-box;margin:0;padding:0}
  html,body{width:1200px;height:1000px;overflow:hidden}
  body{background:var(--backdrop);font-family:'Lato',sans-serif;position:relative;color:var(--ink)}
  .piece{position:absolute}
  .icon{width:7px;height:7px;fill:var(--forest);flex:none}

  /* brand lockup */
  .brand{position:absolute;display:flex;align-items:center;gap:5px;font-family:'Lato',sans-serif;font-weight:700;color:var(--forest);line-height:1.05}
  .brand-dot{border-radius:50%;background:currentColor;flex:none}
  .brand-name{display:block;letter-spacing:.04em;text-transform:uppercase}
  .brand-sub{display:block;letter-spacing:.06em;text-transform:uppercase}

  /* contact blocks */
  .contact{position:absolute;display:flex;gap:8px;font-size:7.4px;color:var(--muted);line-height:9.7px}
  .contact-lines li{list-style:none;display:flex;align-items:center;gap:5px}
  .contact-address{border-left:.8px solid var(--rule);padding-left:8px;align-self:flex-end}
  .contact-address p{white-space:nowrap}

  /* letterhead */
  .letterhead{left:77px;top:161px;width:480px;height:678px;background:var(--paper);box-shadow:0 4px 10px rgba(0,0,0,.35)}
  .letterhead .band{position:absolute;left:0;right:0;bottom:0;height:9px;background:linear-gradient(90deg,var(--forest-deep),var(--forest-light))}
  .letter{position:absolute;left:51px;top:226px;width:377px;font-size:7.7px;line-height:9.7px}
  .letter .salutation{font-weight:700;margin-bottom:10px}
  .letter .para{text-align:justify;margin-bottom:10px}
  .letter .closing{margin-top:27px}
  .letter .signature{font-family:'Pinyon Script',cursive;font-size:15px;line-height:16px;margin-top:10px}
  .letter .title{line-height:9px}

  /* business cards */
  .card{width:224px;height:127px;background:var(--card-black);box-shadow:0 4px 8px rgba(0,0,0,.45);top:202px;color:var(--gold)}
  .card-front{left:572px}
  .card-back{left:811px}
  .card-front .gold-edge{position:absolute;left:0;right:0;bottom:0;height:3px;background:linear-gradient(90deg,#8c6d2a,var(--gold-light),#8c6d2a)}
  .card-front .licence{position:absolute;left:24px;top:80px;width:72px;text-align:center;font-size:4.4px;color:var(--gold)}
  .card-front .divider{position:absolute;left:112px;top:31px;width:.6px;height:65px;background:var(--gold)}
  .card-details{position:absolute;left:121px;top:30px;font-size:4.4px;line-height:6.3px;color:var(--gold)}
  .card-details .person{font-size:6.4px;font-weight:700;line-height:7px}
  .card-details .role{color:#a0885a;margin-bottom:5px}
  .card-details .address{margin-bottom:2px}
  .card-details li{list-style:none;display:flex;align-items:center;gap:3px}
  .card-details .icon{width:4px;height:4px;fill:var(--gold)}
  .partner-badge{position:absolute;left:173px;top:14px;width:28px;height:28px;background:#f2f2f2;border-radius:1px}
  .services{position:absolute;left:21px;top:64px;width:182px;display:flex;justify-content:space-between;font-size:4.4px;line-height:6.3px;color:var(--gold)}
  .services ul{list-style:none}
  .services .rule{width:.6px;background:var(--gold);align-self:stretch;margin-top:2px;height:30px}
  .services .center{text-align:center}
  .services .right{text-align:right}
  .tagline{position:absolute;left:0;right:0;top:109px;text-align:center;font-size:4.8px;font-weight:700;letter-spacing:.02em;color:var(--gold)}

  /* envelopes */
  .envelope-front{left:572px;top:344px;width:552px;height:239px;background:var(--paper);box-shadow:0 4px 10px rgba(0,0,0,.35)}
  .envelope-front .band{position:absolute;left:0;right:0;bottom:0;height:7px;background:linear-gradient(90deg,var(--forest-deep),var(--forest-light))}
  .address-window{position:absolute;left:340px;top:143px;width:174px;height:70px;border-radius:8px;background:linear-gradient(115deg,#cfd0d5,#e6e7eb 45%,var(--window));border:.8px solid #b6b7bd}
  .envelope-back{left:572px;top:600px;width:552px;height:240px;box-shadow:0 4px 10px rgba(0,0,0,.35)}
  .envelope-back svg.body{position:absolute;left:0;top:0}
</style>
</head>
<body>

<svg width="0" height="0" style="position:absolute" aria-hidden="true">
  <symbol id="i-phone" viewBox="0 0 10 10"><path d="M2.2 .8l1.6 1.9-.9 1.1c.6 1.3 1.6 2.3 2.9 2.9l1.1-.9 1.9 1.6-1 1.6C4.4 8.8 1.2 5.6.8 1.8z"/></symbol>
  <symbol id="i-mobile" viewBox="0 0 10 10"><path d="M2.8 0h4.4c.5 0 .8.3.8.8v8.4c0 .5-.3.8-.8.8H2.8c-.5 0-.8-.3-.8-.8V.8c0-.5.3-.8.8-.8zM3 1.2v6.4h4V1.2zM5 8.2a.5.5 0 100 1 .5.5 0 000-1z"/></symbol>
  <symbol id="i-fax" viewBox="0 0 10 10"><path d="M2.5 0h5v3h-5zM1 3.6h8c.5 0 1 .4 1 1V8H8v2H2V8H0V4.6c0-.6.5-1 1-1zM3 6.5v2.6h4V6.5z"/></symbol>
  <symbol id="i-mail" viewBox="0 0 10 10"><path d="M0 2h10v6H0zM.8 2.6L5 5.6l4.2-3z" fill-rule="evenodd"/></symbol>
  <symbol id="i-globe" viewBox="0 0 10 10"><path d="M5 0a5 5 0 110 10A5 5 0 015 0zm-.6 1.1C3.6 2 3.2 3.3 3.1 4.5h1.3zm1.2 0v3.4h1.3c-.1-1.2-.5-2.5-1.3-3.4zM1.1 4.5h1.2c.1-1.1.4-2.2.9-3A4 4 0 001.1 4.5zm5.7-3c.5.8.8 1.9.9 3h1.2a4 4 0 00-2.1-3zM1.1 5.5a4 4 0 002.1 3c-.5-.8-.8-1.9-.9-3zm2 0c.1 1.2.5 2.5 1.3 3.4V5.5zm2.5 0v3.4c.8-.9 1.2-2.2 1.3-3.4zm2.1 0c-.1 1.1-.4 2.2-.9 3a4 4 0 002.1-3z"/></symbol>
</svg>

<!-- Letterhead -->
<section class="piece letterhead">
  <div class="brand" style="left:26px;top:26px">
    <span class="brand-dot" style="width:10px;height:10px"></span>
    <span><span class="brand-name" style="font-size:15px">Kestrel Lane</span><span class="brand-sub" style="font-size:7.2px">Flooring &amp; Interiors</span></span>
  </div>
  <div class="contact" style="left:221px;top:27px">
    <ul class="contact-lines">
      <li><svg class="icon"><use href="#i-phone"/></svg>555.310.4827</li>
      <li><svg class="icon"><use href="#i-mobile"/></svg>555.642.1093</li>
      <li><svg class="icon"><use href="#i-fax"/></svg>555.310.4850</li>
      <li><svg class="icon"><use href="#i-mail"/></svg>office@kestrellaneflooring.com</li>
      <li><svg class="icon"><use href="#i-globe"/></svg>www.kestrellaneflooring.com</li>
    </ul>
    <div class="contact-address">
      <p>Kestrel Lane Flooring &amp; Interiors</p>
      <p>314 Kestrel Lane</p>
      <p>Larkmoor CA 93871</p>
      <p>CA Lic #512784</p>
    </div>
  </div>
  <article class="letter">
    <p class="salutation">Dear Martin Halloway,</p>
    <p class="para">Lorem ipsum dolor sit amet, consectetuer adipiscing elit, sed diam nonummy nibh euismod tincidunt ut laoreet dolore magna aliquam erat volutpat. Ut wisi enim ad minim veniam, quis nostrud exerci tation ullamcorper suscipit lobortis nisl ut aliquip ex ea commodo consequat. Duis dolore te feugait nulla facilisi. Nam liber tempor cum soluta nobis eleifend option congue nihil imperdiet doming id quod mazim placerat facer possim assum. Lorem ipsum dolor sit amet, consectetuer adipiscing elit, sed diam nonummy nibh euismod tincidunt ut laoreet dolore magna aliquam erat volutpat. Ut wisi enim ad minim veniam, quis nostrud exerci tation ullamcorper suscipit lobortis nisl ut aliquip ex ea commodo consequat.</p>
    <p class="para">Consectetuer adipiscing elit, sed diam nonummy nibh euismod tincidunt ut laoreet dolore magna aliquam erat volutpat. Ut wisi enim ad minim veniam, quis nostrud exerci tation ullamcorper suscipit lobortis nisl ut aliquip ex ea commodo consequat. Consectetuer adipiscing elit, sed diam nonummy nibh euismod tincidunt ut laoreet dolore magna aliquam erat volutpat. Ut wisi enim ad minim veniam, quis nostrud exerci tation ullamcorper suscipit lobortis nisl ut aliquip ex ea commodo consequat.</p>
    <p class="para">Consectetuer adipiscing elit, sed diam nonummy nibh euismod tincidunt ut laoreet dolore magna aliquam erat volutpat. Ut wisi enim ad minim veniam, quis nostrud exerci tation ullamcorper suscipit lobortis nisl ut aliquip ex ea commodo consequat. Consectetuer adipiscing elit, sed diam nonummy nibh euismod tincidunt ut laoreet dolore magna aliquam erat volutpat. Ut wisi enim ad minim veniam, quis nostrud exerci tation ullamcorper suscipit lobortis nisl ut aliquip ex ea commodo consequat.</p>
    <p class="closing">Sincerely Yours</p>
    <p class="signature">Owen Castellan</p>
    <p class="title">General Manager</p>
  </article>
  <div class="band"></div>
</section>

<!-- Business card front -->
<section class="piece card card-front">
  <div class="brand" style="left:24px;top:45px;color:var(--gold)">
    <span class="brand-dot" style="width:6px;height:6px"></span>
    <span><span class="brand-name" style="font-size:9.5px">Kestrel Lane</span><span class="brand-sub" style="font-size:4.6px">Flooring &amp; Interiors</span></span>
  </div>
  <p class="licence">CA LIC #512784</p>
  <div class="divider"></div>
  <div class="card-details">
    <p class="person">DANA WRENFIELD</p>
    <p class="role">Salesperson</p>
    <p>314 Kestrel Lane</p>
    <p class="address">Larkmoor CA 93871</p>
    <ul>
      <li><svg class="icon"><use href="#i-phone"/></svg>555.310.4827</li>
      <li><svg class="icon"><use href="#i-mobile"/></svg>555.642.1093</li>
      <li><svg class="icon"><use href="#i-fax"/></svg>555.310.4850</li>
      <li><svg class="icon"><use href="#i-mail"/></svg>office@kestrellaneflooring.com</li>
      <li><svg class="icon"><use href="#i-globe"/></svg>www.kestrellaneflooring.com</li>
    </ul>
  </div>
  <div class="gold-edge"></div>
</section>

<!-- Business card back -->
<section class="piece card card-back">
  <div class="brand" style="left:21px;top:17px;color:var(--gold)">
    <span class="brand-dot" style="width:6px;height:6px"></span>
    <span><span class="brand-name" style="font-size:9.5px">Kestrel Lane</span><span class="brand-sub" style="font-size:4.6px">Flooring &amp; Interiors</span></span>
  </div>
  <div class="partner-badge" role="img" aria-label="Partner dealer badge"></div>
  <div class="services">
    <ul><li>Area Rugs</li><li>Blinds</li><li>Carpet</li><li>Cork</li></ul>
    <span class="rule"></span>
    <ul class="center"><li>Hardwood</li><li>Laminate</li><li>Sheers</li><li>Valances</li></ul>
    <span class="rule"></span>
    <ul class="center"><li>Vinyl</li><li>Bed Spreads</li><li>Draperies</li><li>Fabric</li></ul>
    <span class="rule"></span>
    <ul class="right" style="margin-top:-3px"><li>Motorized Shades</li><li>Pillows</li><li>Shutters</li><li>Upholstery</li><li>Verticals</li></ul>
  </div>
  <p class="tagline">HOME TOWN SERVICE SINCE 1979</p>
</section>

<!-- Envelope front -->
<section class="piece envelope-front">
  <div class="brand" style="left:37px;top:31px">
    <span class="brand-dot" style="width:10px;height:10px"></span>
    <span><span class="brand-name" style="font-size:15px">Kestrel Lane</span><span class="brand-sub" style="font-size:7.2px">Flooring &amp; Interiors</span></span>
  </div>
  <div class="contact" style="left:39px;top:165px">
    <ul class="contact-lines">
      <li><svg class="icon"><use href="#i-phone"/></svg>555.310.4827</li>
      <li><svg class="icon"><use href="#i-mobile"/></svg>555.642.1093</li>
      <li><svg class="icon"><use href="#i-fax"/></svg>555.310.4850</li>
      <li><svg class="icon"><use href="#i-mail"/></svg>office@kestrellaneflooring.com</li>
      <li><svg class="icon"><use href="#i-globe"/></svg>www.kestrellaneflooring.com</li>
    </ul>
    <div class="contact-address">
      <p>Kestrel Lane Flooring &amp; Interiors</p>
      <p>314 Kestrel Lane</p>
      <p>Larkmoor CA 93871</p>
      <p>CA Lic #512784</p>
    </div>
  </div>
  <div class="address-window"></div>
  <div class="band"></div>
</section>

<!-- Envelope back -->
<section class="piece envelope-back">
  <svg class="body" width="552" height="240" viewBox="0 0 552 240">
    <defs>
      <linearGradient id="flap" x1="0" x2="1" y1="0" y2="1">
        <stop offset="0" stop-color="#143a22"/>
        <stop offset="1" stop-color="#245a34"/>
      </linearGradient>
    </defs>
    <rect width="552" height="240" fill="#dcdde4"/>
    <path d="M8 76 L4 236 M544 76 L548 236" stroke="#bfc0c6" stroke-width=".8" fill="none"/>
    <path d="M0 0 H552 L534 64 Q530 78 516 78 H36 Q22 78 18 64 Z" fill="url(#flap)"/>
  </svg>
  <div class="brand" style="left:236px;top:22px;color:#e8e9ee">
    <span class="brand-dot" style="width:7px;height:7px"></span>
    <span><span class="brand-name" style="font-size:9.5px">Kestrel Lane</span><span class="brand-sub" style="font-size:4.6px">Flooring &amp; Interiors</span></span>
  </div>
</section>

</body>
</html>
```